Book Cover for Christian book about open-air preaching

The book is about open-air or outdoor preaching. It is for pastors, evangelists, or any Christian who feels called to share the Gospel with crowds outside of the church. The title is "Quiet Meadows" with a subtitle of "A guide for patient gardening in the distant valley". The Bible verse reference for the title is Jeremiah 20:9. Size will be 9" high by 6"wide
Updates

Went on vacation/holiday

Target Market(s)

Christian pastors, missonaries, evangelists

Industry/Entity Type

religous

Requirements
Must have
• Meet Marlowe Indie Print Services guidelines for book covers

```html
<!DOCTYPE html>
<html lang="en">
<head>
<meta charset="UTF-8">
<title>Quiet Meadows — Book Cover</title>
<link href="https://fonts.googleapis.com/css2?family=Bebas+Neue&family=Cinzel:wght@400&family=Sacramento&family=Montserrat:wght@700&display=swap" rel="stylesheet">
<style>
  :root {
    --page-bg: #2b2b2b;
    --sky-top: #7c6d93;
    --sky-mid: #d9d3e2;
    --paper: #f7f5f1;
    --title-blue: #3a4fa0;
    --subtitle-blue: #233a8c;
    --script-pink: #e8669c;
    --author-white: #ffffff;
    --crowd-red: #e0383c;
    --crowd-pink: #d92a83;
    --crowd-purple: #8c3fa8;
    --crowd-blue: #3a7fd0;
  }
  html, body {
    margin: 0;
    padding: 0;
    width: 1200px;
    height: 905px;
    overflow: hidden;
    background: var(--page-bg);
  }
  .canvas {
    position: relative;
    width: 1200px;
    height: 905px;
  }
  .cover {
    position: absolute;
    left: 318px;
    top: 30px;
    width: 563px;
    height: 845px;
    overflow: hidden;
    background:
      radial-gradient(ellipse 60% 30% at 20% 10%, rgba(214,120,150,0.35), transparent 70%),
      radial-gradient(ellipse 70% 25% at 70% 55%, rgba(190,200,230,0.35), transparent 70%),
      linear-gradient(180deg, var(--sky-top) 0%, #a99cb6 8%, var(--sky-mid) 22%, var(--paper) 40%, var(--paper) 62%, #f1e8f1 75%);
  }
  .author-name {
    position: absolute;
    top: 42px;
    left: 0;
    right: 0;
    margin: 0;
    text-align: center;
    font-family: 'Bebas Neue', sans-serif;
    font-size: 48px;
    letter-spacing: 11px;
    color: var(--author-white);
    font-weight: 400;
  }
  .birds {
    position: absolute;
    top: 28px;
    left: 150px;
    width: 170px;
    height: 100px;
    border-radius: 50%;
    background: radial-gradient(ellipse at 60% 40%, rgba(190,90,60,0.35), transparent 70%);
  }
  .title {
    position: absolute;
    top: 218px;
    left: 0;
    right: 0;
    margin: 0;
    text-align: center;
    font-weight: 400;
  }
  .title-main {
    display: block;
    font-family: 'Cinzel', serif;
    font-size: 66px;
    letter-spacing: 12px;
    color: var(--title-blue);
    line-height: 1;
  }
  .title-script {
    display: block;
    margin-top: -6px;
    font-family: 'Sacramento', cursive;
    font-size: 78px;
    color: var(--script-pink);
    line-height: 1;
  }
  .subtitle {
    position: absolute;
    top: 452px;
    left: 60px;
    right: 60px;
    margin: 0;
    text-align: center;
    font-family: 'Montserrat', sans-serif;
    font-weight: 700;
    font-size: 16px;
    line-height: 1.35;
    text-transform: uppercase;
    color: var(--subtitle-blue);
  }
  .crowd {
    position: absolute;
    left: 0;
    bottom: 0;
    width: 563px;
    height: 290px;
  }
</style>
</head>
<body>
  <div class="canvas">
    <div class="cover">
      <div class="birds" role="img" aria-label="Small flock of birds flying across the sky"></div>
      <p class="author-name">Author Name</p>
      <h1 class="title">
        <span class="title-main">QUIET</span>
        <span class="title-script">meadows</span>
      </h1>
      <p class="subtitle">A guide for patient gardening<br>in the distant valley</p>
      <svg class="crowd" viewBox="0 0 563 290" role="img" aria-label="Colourful silhouette of a cheering crowd with raised arms">
        <defs>
          <linearGradient id="crowdTone" x1="0" y1="0" x2="1" y2="1">
            <stop offset="0" stop-color="var(--crowd-red)"/>
            <stop offset="0.45" stop-color="var(--crowd-pink)"/>
            <stop offset="0.8" stop-color="var(--crowd-purple)"/>
            <stop offset="1" stop-color="var(--crowd-blue)"/>
          </linearGradient>
          <linearGradient id="crowdFade" x1="0" y1="0" x2="0" y2="1">
            <stop offset="0" stop-color="#fff" stop-opacity="0"/>
            <stop offset="0.35" stop-color="#fff" stop-opacity="1"/>
          </linearGradient>
          <mask id="crowdMask">
            <rect width="563" height="290" fill="url(#crowdFade)"/>
          </mask>
        </defs>
        <rect width="563" height="290" fill="url(#crowdTone)" mask="url(#crowdMask)"/>
      </svg>
    </div>
  </div>
</body>
</html>
```